The most modern business card ever !!!

Our company call “Vantilo”. Vantilo is a technology company specialized in cruises solutions. Out main product is a platform to reserve cruises. This is a revolutionary platform that make easier to travel agencies and final users to reserve cruises across dozen companies like tarvik, welbi, dpv, hbt, etc..We are a “start up”, with a young team of developers and we want to transmit it.. For it, we want something different, a modern business card that represent cruises and technology.. When someone receive this card, this person should say: wowww this is different… this is modern… this is a cruise related company..
Contact Information for Business Card
Requirements
Must have
- diferent, modern
Should not have
- traditions business card

```html
<!DOCTYPE html>
<html lang="en">
<head>
<meta charset="utf-8">
<title>Vantilo Business Card</title>
<link href="https://fonts.googleapis.com/css2?family=Marcellus+SC&display=swap" rel="stylesheet">
<style>
  :root {
    --page: #ffffff;
    --card: #808080;
    --ink: #000000;
    --edge: #000000;
  }
  html, body {
    margin: 0;
    padding: 0;
    width: 1200px;
    height: 1000px;
    overflow: hidden;
    background: var(--page);
  }
  .canvas {
    position: relative;
    width: 1200px;
    height: 1000px;
    font-family: "Marcellus SC", serif;
    color: var(--ink);
  }
  .card {
    position: absolute;
    box-sizing: border-box;
    background: var(--card);
    border: 8px solid var(--edge);
  }
  .card--front {
    left: 80px;
    top: 55px;
    width: 730px;
    height: 420px;
    border-radius: 0 0 0 200px;
  }
  .card--back {
    left: 378px;
    top: 513px;
    width: 732px;
    height: 422px;
    border-radius: 0 0 200px 0;
  }
  .emblem {
    position: absolute;
    width: 324px;
    height: 324px;
    border-radius: 50%;
    background: var(--ink);
  }
  .card--front .emblem { left: 206px; top: 38px; transform: translateX(-160px); }
  .card--back .emblem { left: 343px; top: 42px; }
  .brand {
    position: absolute;
    left: 440px;
    top: 148px;
    margin: 0;
    font-size: 50px;
    font-weight: 400;
    line-height: 1;
    letter-spacing: 1px;
  }
  .slogan {
    position: absolute;
    left: 442px;
    top: 203px;
    margin: 0;
    font-size: 21px;
    letter-spacing: 1px;
  }
  .contact {
    position: absolute;
    left: 30px;
    top: 56px;
    width: 268px;
    text-align: center;
  }
  .contact__name {
    margin: 0;
    font-size: 34px;
    font-weight: 400;
    line-height: 1;
    letter-spacing: 1.5px;
  }
  .contact__title {
    margin: 3px 0 0;
    font-size: 17px;
    letter-spacing: 1px;
  }
  .contact__lines {
    margin: 44px 0 0;
    font-size: 17px;
    line-height: 20.5px;
    letter-spacing: 1px;
  }
  .contact__lines + .contact__lines { margin-top: 20px; }
</style>
</head>
<body>
<div class="canvas">
  <section class="card card--front">
    <div class="emblem" aria-hidden="true"></div>
    <h1 class="brand">Vantilo</h1>
    <p class="slogan">Your Slogan Here</p>
  </section>

  <section class="card card--back">
    <div class="contact">
      <h2 class="contact__name">Your Name</h2>
      <p class="contact__title">Your Title</p>
      <p class="contact__lines">1 111-111-1111<br>yourwebsite.com<br>youremail@website.com</p>
      <p class="contact__lines">111 Address<br>Building/Suite Number<br>City, State Zip Code</p>
      <p class="contact__lines">Social Media Address</p>
    </div>
    <div class="emblem" aria-hidden="true"></div>
  </section>
</div>
</body>
</html>
```